Financial Services Sales Sheet

We need this sheet redesigned. Needs to feel very corporate/financial. open to imagery/icons/colors/etc. Copy is in the docx file to expedite work. PDF is what client has done inh-house and feels dated.

```html
<!DOCTYPE html>
<html lang="en">
<head>
<meta charset="utf-8">
<title>Harbor Ledger Advisors – Master Servicing &amp; Portfolio Optimization</title>
<link rel="stylesheet" href="https://fonts.googleapis.com/css2?family=Montserrat:wght@600;700;800&family=Inter:wght@400;500;600;700&display=swap">
<style>
  :root{
    --navy:#0d2c55;
    --navy-deep:#0a2142;
    --navy-ink:#11223d;
    --blue:#1d5fa8;
    --steel:#5d7fa6;
    --page:#ffffff;
    --card-top:#fbfcfd;
    --card-bot:#dfe4ea;
    --card-line:#c6ccd4;
    --text:#1b2432;
    --muted:#3c4656;
    --backdrop:#0f2a4a;
  }
  *{box-sizing:border-box;margin:0;padding:0}
  html,body{width:1200px;height:1200px;overflow:hidden}
  body{background:var(--backdrop);font-family:"Inter",Arial,sans-serif;color:var(--text)}
  .sheet{position:absolute;left:210px;top:32px;width:780px;height:1136px;background:var(--page);overflow:hidden;box-shadow:0 10px 40px rgba(0,0,0,.35)}
  .hero-visual{position:absolute;right:0;top:0;width:380px;height:300px;
    background:linear-gradient(200deg,#c9d6e6 0%,#e8eef5 45%,rgba(255,255,255,0) 80%)}
  .brand{position:absolute;left:42px;top:62px;display:flex;align-items:center;gap:14px}
  .brand-mark{width:34px;height:34px;background:var(--navy)}
  .brand-name{font-family:"Montserrat",Arial,sans-serif;font-weight:700;font-size:21px;line-height:1.1;color:var(--navy);text-transform:uppercase}
  .headline{position:absolute;left:42px;top:140px;font-family:"Montserrat",Arial,sans-serif;font-weight:800;font-size:50px;line-height:1.08;color:var(--navy-ink);letter-spacing:-.5px}
  .subhead{position:absolute;left:42px;top:262px;font-family:"Inter",Arial,sans-serif;font-weight:600;font-size:19px;color:var(--navy-ink)}
  .intro{position:absolute;left:42px;top:302px;width:700px;font-size:16px;line-height:1.4;color:var(--muted)}
  .services{position:absolute;left:42px;top:372px;display:flex;gap:18px}
  .service{width:224px;height:240px;border-radius:8px;background:linear-gradient(180deg,var(--card-top),var(--card-bot));border:1px solid var(--card-line);box-shadow:0 3px 8px rgba(20,40,70,.18);padding:16px 14px 14px 16px;overflow:hidden}
  .service svg{width:32px;height:32px;display:block;margin-bottom:12px}
  .service h3{font-weight:700;font-size:16.5px;line-height:1.22;color:var(--navy-ink);padding-bottom:8px;border-bottom:1px solid var(--card-line);margin-bottom:9px;white-space:nowrap;letter-spacing:-.1px}
  .service ul{list-style:none}
  .service li{font-size:14px;line-height:1.3;padding-left:12px;position:relative;margin-bottom:3px}
  .service li::before{content:"•";position:absolute;left:0}
  .snapshot-title{position:absolute;left:42px;top:633px;font-family:"Montserrat",Arial,sans-serif;font-weight:700;font-size:25px;color:var(--navy-ink)}
  .stats{position:absolute;left:42px;top:676px;display:flex;gap:14px}
  .stat{width:154px;height:104px;border-radius:8px;background:linear-gradient(180deg,var(--card-top),var(--card-bot));border:1px solid var(--card-line);box-shadow:0 3px 8px rgba(20,40,70,.18);text-align:center;padding-top:12px}
  .stat:nth-child(2){width:188px}
  .stat:nth-child(3){width:162px}
  .stat:nth-child(4){width:154px}
  .stat-value{font-family:"Inter",Arial,sans-serif;font-weight:700;font-size:29px;line-height:1.05;color:var(--navy-ink)}
  .stat-unit{font-weight:700;font-size:21px;line-height:1.1;color:var(--navy-ink)}
  .stat-label{font-size:14px;line-height:1.2;color:var(--muted);margin-top:4px}
  .platform{position:absolute;left:0;top:804px;width:780px;height:252px;background:var(--navy)}
  .platform-visual{position:absolute;right:0;top:0;width:430px;height:252px;background:linear-gradient(90deg,var(--navy) 0%,#1f3f66 30%,#3a5f8a 65%,#5b7ea8 100%)}
  .platform-copy{position:absolute;left:42px;top:22px;width:340px;color:#fff}
  .platform-name{font-family:"Montserrat",Arial,sans-serif;font-weight:700;font-size:41px;line-height:1.1}
  .platform-tagline{font-size:21px;line-height:1.25;margin-top:10px;color:#e6edf6}
  .platform-desc{font-size:14.5px;line-height:1.35;margin-top:16px;color:#d5deea}
  .footer{position:absolute;left:0;top:1056px;width:780px;height:80px;background:var(--navy-deep);text-align:center;color:#fff;padding-top:14px}
  .footer-cta{font-weight:700;font-size:22px}
  .footer-contact{font-size:16px;margin-top:8px;color:#dbe3ee}
</style>
</head>
<body>
<article class="sheet">
  <div class="hero-visual" role="img" aria-label="Portfolio analytics dashboard screens with charts and figures"></div>

  <header class="brand">
    <span class="brand-mark"></span>
    <span class="brand-name">Harbor Ledger<br>Advisors</span>
  </header>

  <h1 class="headline">Master Servicing &amp;<br>Portfolio Optimization</h1>
  <p class="subhead">End-to-End Post Default Management Strategy, Recovery &amp; Compliance</p>
  <p class="intro">Harbor Ledger Advisors delivers one connected solution across compliance, portfolio analytics, dashboards, and financial servicing to protect value and manage compliance.</p>

  <section class="services">
    <div class="service">
      <svg viewBox="0 0 36 36" fill="none" stroke="#0d2c55" stroke-width="1.6">
        <path d="M4 32h28"/><rect x="7" y="22" width="4" height="10"/><rect x="14" y="17" width="4" height="15"/><rect x="21" y="12" width="4" height="20"/>
        <path d="M6 16l8-6 6 4 10-9"/><path d="M25 5h5v5"/>
      </svg>
      <h3>Strategy &amp; Recovery<br>Optimization</h3>
      <ul><li>Maximizing cash flow</li><li>Recovery analysis</li><li>Recovery scenarios &amp; analysis</li></ul>
    </div>
    <div class="service">
      <svg viewBox="0 0 36 36" fill="none" stroke="#0d2c55" stroke-width="1.6">
        <path d="M8 3h14l6 6v15"/><path d="M8 3v30h12"/><path d="M22 3v6h6"/><path d="M12 14h12M12 19h12M12 24h6"/>
        <circle cx="27" cy="28" r="6"/><path d="M24.5 28l2 2 3.5-4"/>
      </svg>
      <h3>Compliance &amp;<br>Risk Oversight</h3>
      <ul><li>Regulatory compliance</li><li>Audit management</li><li>Reporting &amp; reporting</li></ul>
    </div>
    <div class="service">
      <svg viewBox="0 0 36 36" fill="none" stroke="#0d2c55" stroke-width="1.6">
        <circle cx="18" cy="7" r="4"/><circle cx="7" cy="28" r="4"/><circle cx="29" cy="28" r="4"/>
        <path d="M18 11v8M7 24v-5h22v5"/>
      </svg>
      <h3>Operations &amp; Portfolio<br>Management</h3>
      <ul><li>Scalable workflows</li><li>Servicer performance monitoring</li><li>Financial operations monitoring</li></ul>
    </div>
  </section>

  <h2 class="snapshot-title">Performance Snapshot</h2>
  <section class="stats">
    <div class="stat"><div class="stat-value">$155+</div><div class="stat-unit">Million</div><div class="stat-label">Modern UI metrics</div></div>
    <div class="stat"><div class="stat-value">573,000+</div><div class="stat-label">Minimum<br>infographics</div></div>
    <div class="stat"><div class="stat-value">3,700+</div><div class="stat-label">Largest metrics<br>on modern UI</div></div>
    <div class="stat"><div class="stat-value">21%</div><div class="stat-label">Elegant<br>infographic styling</div></div>
  </section>

  <section class="platform">
    <div class="platform-visual" role="img" aria-label="Operations command center with analysts working at multiple data monitors"></div>
    <div class="platform-copy">
      <div class="platform-name">SignalDeck™</div>
      <div class="platform-tagline">The Intelligence Behind Every Compliant Command.</div>
      <p class="platform-desc">An institutional command center with military-grade operations aesthetic, organized data form AI-powered intelligence dashboard, calm, focused atmosphere.</p>
    </div>
  </section>

  <footer class="footer">
    <div class="footer-cta">Secure Your Portfolio's Future. Partner with HLA Today.</div>
    <div class="footer-contact">harborledgeradvisors.com | contact@hla-advisors.com</div>
  </footer>
</article>
</body>
</html>
```